Banner Ad Design

We require a banner ad design for 4 Brands.

Banner 1: Willowmere on the Heath
Please follow url http://www.goldenyearsresidences.example/index.php/willowmere-on-the-heath/welcome for art, logo, tagline.

Banner 2: Noble Brookhaven
Please follow url http://www.goldenyearsresidences.example/index.php/noble-brookhaven/welcome for art, logo, tagline.

Banner 3: Brookhaven Meadows
Please follow url http://www.goldenyearsresidences.example/index.php/brookhaven-meadows/welcome for art, logo, tagline.

Banner 4: Hartwell Court
http://www.goldenyearsresidences.example/index.php/hartwell-court/welcome

ALL Banners consists of - 1. LOGO, 2. TAGLINE: Experience and uncompromising Retirement Lifestyle. 3. CALL TO ACTION: View Images, Download the Brochure, Register for More.

Each brand must be broken into the following Sizes:

468 × 60
728 × 90
250 × 250
200 × 200
336 × 280
300 × 250
120 × 600
160 × 600
300 × 600
970 × 90
240 × 400
980 × 120
930 × 180
250 × 360
580 × 400
150kb max size

Target Market(s)

Seniors and their middle age children

Industry/Entity Type

Royal

Requirements
Must have
• 468 × 60
728 × 90
250 × 250
200 × 200
336 × 280
300 × 250
120 × 600
160 × 600
300 × 600
970 × 90
240 × 400
980 × 120
930 × 180
250 × 360
580 × 400
150kb max size
Nice to have
• large font for easy viewing - images of the experience
Should not have
• any pictures of decrepit people, or dying people - must be fun and vibrant.

```html
<!DOCTYPE html>
<html lang="en">
<head>
<meta charset="utf-8">
<title>Brookhaven Meadows – Banner Set</title>
<link rel="stylesheet" href="https://fonts.googleapis.com/css2?family=Tinos:wght@400;700&display=swap">
<style>
:root{
  --stage:#e8e3db;
  --purple:#4b2d7f;
  --purple-deep:#3c2268;
  --lavender:#8f73c4;
  --gold:#c8a04a;
  --gold-light:#ecd596;
  --white:#ffffff;
  --orange-top:#fba043;
  --orange-bottom:#e7650f;
  --ink:#2a2a2a;
  --water-deep:#4f7fa3;
  --water-light:#b8cfe1;
  --wood-dark:#6b4a33;
  --wood-light:#c49a72;
  --lounge-dark:#7a5a48;
  --lounge-light:#d8bfa4;
}
*{box-sizing:border-box;margin:0;padding:0}
html,body{width:1200px;height:1107px;overflow:hidden}
body{background:var(--stage);font-family:"Tinos","Times New Roman",serif;position:relative}

.banner{position:absolute;overflow:hidden;background:var(--purple);box-shadow:0 3px 10px rgba(0,0,0,.25)}
.layer{position:absolute;left:0;top:0}
.photo{position:absolute}
.photo--spa{background:linear-gradient(160deg,var(--water-light),var(--water-deep))}
.photo--billiards{background:linear-gradient(150deg,var(--wood-light),var(--wood-dark))}
.photo--lounge{background:linear-gradient(170deg,var(--lounge-light),var(--lounge-dark))}
.panel-white{position:absolute;background:var(--white)}

.copy{position:absolute;text-align:center;color:var(--white);text-transform:uppercase;line-height:1.05}
.copy .title{font-weight:400;letter-spacing:.5px}
.copy .title--line{white-space:nowrap}
.copy .rule{border:0;height:2px;margin:0 auto;background:linear-gradient(90deg,transparent,rgba(255,255,255,.75),transparent)}
.copy .tagline span{display:block;white-space:nowrap}
.copy .tagline .strong{font-weight:700}

.logo{position:absolute;color:var(--purple);font-weight:400;text-align:center;line-height:1.05}
.logo span{display:block;white-space:nowrap}

.cta{position:absolute;display:flex;align-items:center;justify-content:space-between;white-space:nowrap;
  background:linear-gradient(var(--orange-top),var(--orange-bottom));color:var(--white);
  border-radius:4px;box-shadow:0 2px 3px rgba(0,0,0,.3);font-family:"Arial",sans-serif}
.cta svg{flex:none}

.strip-lavender{position:absolute;background:linear-gradient(90deg,var(--purple),var(--lavender),var(--purple))}
</style>
</head>
<body>

<!-- 300 x 600 -->
<div class="banner" style="left:45px;top:52px;width:398px;height:796px">
  <div class="photo photo--spa" style="left:0;top:0;width:227px;height:165px" role="img" aria-label="Photo: smiling senior woman relaxing in a hot tub"></div>
  <div class="photo photo--billiards" style="left:231px;top:0;width:167px;height:165px" role="img" aria-label="Photo: senior man lining up a billiards shot"></div>
  <div class="photo photo--lounge" style="left:0;top:170px;width:398px;height:190px" role="img" aria-label="Photo: residents attending a talk in a lounge"></div>
  <svg class="layer" width="398" height="796" viewBox="0 0 398 796">
    <path d="M0,235 Q140,372 398,318 L398,672 L0,672 Z" fill="var(--purple)"/>
    <path d="M0,235 Q140,372 398,318" fill="none" stroke="var(--gold)" stroke-width="6"/>
    <path d="M0,243 Q140,380 398,326" fill="none" stroke="var(--gold-light)" stroke-width="1.5"/>
  </svg>
  <div class="copy" style="left:0;width:398px;top:420px">
    <div class="title title--line" style="font-size:28px">Brookhaven Meadows</div>
    <hr class="rule" style="width:200px;margin-top:20px;margin-bottom:26px">
    <div class="tagline">
      <span style="font-size:31px">Experience and</span>
      <span style="font-size:31px">Uncompromising</span>
      <span style="font-size:31px">Retirement</span>
      <span class="strong" style="font-size:50px">Lifestyle</span>
    </div>
  </div>
  <div class="strip-lavender" style="left:0;top:664px;width:398px;height:8px"></div>
  <div class="panel-white" style="left:0;top:672px;width:398px;height:124px"></div>
  <div class="logo" style="left:10px;top:712px;width:130px;font-size:20px"><span>Willowmere</span><span>on the Heath</span></div>
  <div class="cta" style="left:141px;top:719px;width:242px;height:56px;padding:0 14px 0 18px;font-size:20px">Register for More
    <svg width="32" height="32" viewBox="0 0 32 32"><circle cx="16" cy="16" r="15" fill="var(--white)"/><path d="M13,9 L20,16 L13,23" fill="none" stroke="var(--ink)" stroke-width="4"/></svg>
  </div>
</div>

<!-- 160 x 600 -->
<div class="banner" style="left:468px;top:52px;width:212px;height:796px">
  <div class="photo photo--billiards" style="left:0;top:0;width:212px;height:131px" role="img" aria-label="Photo: senior man lining up a billiards shot"></div>
  <div class="photo photo--spa" style="left:0;top:131px;width:212px;height:150px" role="img" aria-label="Photo: smiling senior woman relaxing in a hot tub"></div>
  <svg class="layer" width="212" height="796" viewBox="0 0 212 796">
    <path d="M0,228 Q106,330 212,228 L212,652 L0,652 Z" fill="var(--purple)"/>
    <path d="M0,228 Q106,330 212,228" fill="none" stroke="var(--gold)" stroke-width="5"/>
  </svg>
  <div class="copy" style="left:0;width:212px;top:340px">
    <div class="title" style="font-size:24px;line-height:1.35">Brookhaven<br>Meadows</div>
    <hr class="rule" style="width:150px;margin-top:14px;margin-bottom:18px">
    <div class="tagline">
      <span style="font-size:26px">Experience</span>
      <span style="font-size:18px;margin-top:2px">And</span>
      <span style="font-size:18px;margin-top:2px">Uncompromising</span>
      <span style="font-size:25px;margin-top:2px">Retirement</span>
      <span class="strong" style="font-size:25px;margin-top:4px">Lifestyle</span>
    </div>
  </div>
  <div class="cta" style="left:13px;top:581px;width:184px;height:42px;padding:0 8px 0 12px;font-size:15px">Register for More
    <svg width="26" height="26" viewBox="0 0 32 32"><circle cx="16" cy="16" r="15" fill="var(--white)"/><path d="M13,9 L20,16 L13,23" fill="none" stroke="var(--ink)" stroke-width="4"/></svg>
  </div>
  <div class="strip-lavender" style="left:0;top:644px;width:212px;height:8px"></div>
  <div class="panel-white" style="left:0;top:652px;width:212px;height:144px"></div>
  <div class="logo" style="left:0;top:690px;width:212px;font-size:24px"><span>Willowmere</span><span>on the Heath</span></div>
</div>

<!-- 336 x 280 -->
<div class="banner" style="left:706px;top:78px;width:446px;height:371px">
  <div class="panel-white" style="left:0;top:0;width:240px;height:161px"></div>
  <div class="photo photo--spa" style="left:0;top:161px;width:240px;height:210px" role="img" aria-label="Photo: smiling senior woman relaxing in a hot tub"></div>
  <svg class="layer" width="446" height="371" viewBox="0 0 446 371">
    <path d="M198,0 Q262,180 225,371 L446,371 L446,0 Z" fill="var(--purple)"/>
    <path d="M198,0 Q262,180 225,371" fill="none" stroke="var(--gold)" stroke-width="5"/>
  </svg>
  <div class="logo" style="left:0;top:48px;width:200px;font-size:25px"><span>Willowmere</span><span>on the Heath</span></div>
  <div class="copy" style="left:246px;width:200px;top:14px">
    <div class="title" style="font-size:26px;line-height:1.3">Brookhaven<br>Meadows</div>
    <hr class="rule" style="width:150px;margin-top:8px;margin-bottom:14px">
    <div class="tagline">
      <span style="font-size:24px">Experience</span>
      <span style="font-size:17px;margin-top:4px">And</span>
      <span style="font-size:17px;margin-top:4px">Uncompromising</span>
      <span style="font-size:23px;margin-top:4px">Retirement</span>
      <span class="strong" style="font-size:23px;margin-top:5px">Lifestyle</span>
    </div>
  </div>
  <div class="strip-lavender" style="left:232px;top:282px;width:214px;height:10px"></div>
  <div class="panel-white" style="left:236px;top:292px;width:210px;height:79px"></div>
  <div class="cta" style="left:239px;top:314px;width:183px;height:43px;padding:0 8px 0 12px;font-size:15px">Register for More
    <svg width="26" height="26" viewBox="0 0 32 32"><circle cx="16" cy="16" r="15" fill="var(--white)"/><path d="M13,9 L20,16 L13,23" fill="none" stroke="var(--ink)" stroke-width="4"/></svg>
  </div>
</div>

<!-- 300 x 250 -->
<div class="banner" style="left:730px;top:465px;width:398px;height:332px">
  <div class="panel-white" style="left:0;top:0;width:215px;height:149px"></div>
  <div class="photo photo--spa" style="left:0;top:149px;width:215px;height:183px" role="img" aria-label="Photo: smiling senior woman relaxing in a hot tub"></div>
  <svg class="layer" width="398" height="332" viewBox="0 0 398 332">
    <path d="M200,0 Q248,160 210,332 L398,332 L398,0 Z" fill="var(--purple)"/>
    <path d="M200,0 Q248,160 210,332" fill="none" stroke="var(--gold)" stroke-width="5"/>
  </svg>
  <div class="logo" style="left:0;top:50px;width:190px;font-size:22px"><span>Willowmere</span><span>on the Heath</span></div>
  <div class="copy" style="left:226px;width:172px;top:12px">
    <div class="title" style="font-size:22px;line-height:1.3">Brookhaven<br>Meadows</div>
    <hr class="rule" style="width:140px;margin-top:6px;margin-bottom:12px">
    <div class="tagline">
      <span style="font-size:22px">Experience</span>
      <span style="font-size:15px;margin-top:4px">And</span>
      <span style="font-size:15px;margin-top:3px">Uncompromising</span>
      <span style="font-size:20px;margin-top:3px">Retirement</span>
      <span class="strong" style="font-size:20px;margin-top:4px">Lifestyle</span>
    </div>
  </div>
  <div class="strip-lavender" style="left:216px;top:252px;width:182px;height:9px"></div>
  <div class="panel-white" style="left:218px;top:261px;width:180px;height:71px"></div>
  <div class="cta" style="left:222px;top:280px;width:160px;height:37px;padding:0 7px 0 10px;font-size:13px">Register for More
    <svg width="22" height="22" viewBox="0 0 32 32"><circle cx="16" cy="16" r="15" fill="var(--white)"/><path d="M13,9 L20,16 L13,23" fill="none" stroke="var(--ink)" stroke-width="4"/></svg>
  </div>
</div>

<!-- 468 x 60 -->
<div class="banner" style="left:45px;top:872px;width:622px;height:77px">
  <div class="panel-white" style="left:0;top:0;width:106px;height:77px"></div>
  <div class="photo photo--spa" style="left:106px;top:0;width:170px;height:77px" role="img" aria-label="Photo: smiling senior woman relaxing in a hot tub"></div>
  <svg class="layer" width="622" height="77" viewBox="0 0 622 77">
    <path d="M250,0 Q272,38 260,77 L622,77 L622,0 Z" fill="var(--purple)"/>
    <path d="M250,0 Q272,38 260,77" fill="none" stroke="var(--gold)" stroke-width="4"/>
  </svg>
  <div class="logo" style="left:0;top:21px;width:106px;font-size:13px"><span>Willowmere</span><span>on the Heath</span></div>
  <div class="copy" style="left:266px;width:230px;top:7px">
    <div class="title title--line" style="font-size:16px">Brookhaven Meadows</div>
    <hr class="rule" style="width:150px;margin-top:5px;margin-bottom:6px">
    <div class="tagline" style="font-size:11.5px">
      <span>Experience and Uncompromising</span>
      <span style="margin-top:3px">Retirement <b class="strong">Lifestyle</b></span>
    </div>
  </div>
  <div class="cta" style="left:500px;top:31px;width:117px;height:28px;padding:0 5px 0 7px;font-size:10px;border-radius:3px">Register for More
    <svg width="17" height="17" viewBox="0 0 32 32"><circle cx="16" cy="16" r="15" fill="var(--white)"/><path d="M13,9 L20,16 L13,23" fill="none" stroke="var(--ink)" stroke-width="4"/></svg>
  </div>
</div>

<!-- 728 x 90 -->
<div class="banner" style="left:45px;top:957px;width:968px;height:118px">
  <div class="panel-white" style="left:0;top:0;width:165px;height:118px"></div>
  <div class="photo photo--spa" style="left:165px;top:0;width:250px;height:118px" role="img" aria-label="Photo: smiling senior woman relaxing in a hot tub"></div>
  <svg class="layer" width="968" height="118" viewBox="0 0 968 118">
    <path d="M375,0 Q408,60 392,118 L968,118 L968,0 Z" fill="var(--purple)"/>
    <path d="M375,0 Q408,60 392,118" fill="none" stroke="var(--gold)" stroke-width="5"/>
  </svg>
  <div class="logo" style="left:0;top:36px;width:165px;font-size:21px"><span>Willowmere</span><span>on the Heath</span></div>
  <div class="copy" style="left:400px;width:375px;top:10px">
    <div class="title title--line" style="font-size:28px">Brookhaven Meadows</div>
    <hr class="rule" style="width:240px;margin-top:9px;margin-bottom:11px">
    <div class="tagline" style="font-size:17px">
      <span>Experience and Uncompromising</span>
      <span style="margin-top:5px">Retirement <b class="strong">Lifestyle</b></span>
    </div>
  </div>
  <div class="cta" style="left:779px;top:49px;width:181px;height:42px;padding:0 8px 0 13px;font-size:16px">Register for More
    <svg width="26" height="26" viewBox="0 0 32 32"><circle cx="16" cy="16" r="15" fill="var(--white)"/><path d="M13,9 L20,16 L13,23" fill="none" stroke="var(--ink)" stroke-width="4"/></svg>
  </div>
</div>

</body>
</html>
```